Bright Oak Fitness Facility Business Cards

Business Card Design that incorporates the logo and tagline

Target Market(s)

Fitness, People Who Exercise

Contact Information for Business Card

2718 Harrow Creek Bend
Linwood Falls, Ohio 43090
Phone: 614-555-Team (8326)
www.brightoakfitness.example
info@brightoakfitness.example

Requirements
Must have
• Logo, Address, Website, email and tagline "Stronger Every Day". Colors should be red/black/grey/white

```html
<!DOCTYPE html>
<html lang="en">
<head>
<meta charset="utf-8">
<title>Bright Oak Fitness – Business Cards</title>
<link rel="stylesheet" href="https://fonts.googleapis.com/css2?family=Open+Sans:wght@400;600;700;800&display=swap">
<style>
  :root {
    --backdrop: #2b2d30;
    --card-black: #0d0d0e;
    --card-white: #ffffff;
    --brand-red: #ef2127;
    --ink-grey: #c9c9c9;
    --text-white: #ffffff;
  }
  html, body {
    margin: 0;
    width: 1200px;
    height: 900px;
    overflow: hidden;
    background: var(--backdrop);
    font-family: "Open Sans", Arial, sans-serif;
  }
  .canvas {
    position: relative;
    width: 1200px;
    height: 900px;
    display: flex;
    align-items: center;
    justify-content: center;
    gap: 60px;
  }
  .card {
    width: 520px;
    height: 297px;
    display: block;
    box-shadow: 0 10px 30px rgba(0,0,0,.45);
  }
  .card text { font-family: "Open Sans", Arial, sans-serif; }
  .brand-name { font-weight: 800; fill: var(--card-black); }
  .tagline { font-weight: 600; fill: var(--text-white); }
  .person-name { font-weight: 700; fill: var(--brand-red); letter-spacing: .5px; }
  .person-title { font-weight: 400; fill: var(--text-white); letter-spacing: 1px; }
  .contact { font-weight: 400; fill: var(--text-white); }
  .address { font-weight: 600; fill: var(--text-white); }
  .back-name { font-weight: 800; fill: var(--text-white); }
  .handle { font-weight: 600; fill: var(--brand-red); }
</style>
</head>
<body>
<main class="canvas">

  <svg class="card card-front" viewBox="0 0 520 297" xmlns="http://www.w3.org/2000/svg">
    <rect width="520" height="297" fill="var(--card-white)"/>
    <path class="dark-base" d="M0,150 Q260,70 520,150 L520,297 L0,297 Z" fill="var(--card-black)"/>
    <path id="arc-band" d="M0,140 Q260,60 520,140" fill="none" stroke="var(--brand-red)" stroke-width="24"/>
    <path id="arc-text" d="M0,145 Q260,65 520,145" fill="none"/>

    <g class="logo-lockup">
      <circle cx="152" cy="62" r="9" fill="var(--brand-red)"/>
      <text class="brand-name" x="172" y="71" font-size="26">Bright Oak Fitness</text>
    </g>

    <text class="tagline" font-size="13">
      <textPath href="#arc-text" startOffset="50%" text-anchor="middle">Stronger Every Day</textPath>
    </text>

    <text class="person-name" x="260" y="162" font-size="19" text-anchor="middle">MARCUS HALE</text>
    <text class="person-title" x="260" y="179" font-size="10" text-anchor="middle">DIRECTOR</text>

    <g class="contact-details">
      <text class="contact" x="246" y="216" font-size="11" text-anchor="end">614-555-Team (8326)</text>
      <text class="contact" x="246" y="236" font-size="11" text-anchor="end">info@brightoakfitness.example</text>
      <text class="contact" x="246" y="262" font-size="11" text-anchor="end">www.<tspan fill="var(--brand-red)" font-weight="700">BRIGHTOAK</tspan>FITNESS.EXAMPLE</text>
      <line x1="260" y1="204" x2="260" y2="244" stroke="var(--brand-red)" stroke-width="2"/>
      <text class="address" x="274" y="219" font-size="13">2718 Harrow Creek Bend</text>
      <text class="address" x="274" y="238" font-size="13">Linwood Falls, Ohio 43090</text>
    </g>
  </svg>

  <svg class="card card-back" viewBox="0 0 520 297" xmlns="http://www.w3.org/2000/svg">
    <rect width="520" height="297" fill="var(--card-black)"/>
    <g class="logo-lockup">
      <circle cx="118" cy="138" r="12" fill="var(--brand-red)"/>
      <text class="back-name" x="142" y="150" font-size="32">Bright Oak Fitness</text>
    </g>
    <text class="handle" x="260" y="190" font-size="15" text-anchor="middle">@brightoakfitness</text>
  </svg>

</main>
</body>
</html>
```